Gum Creek Critters business card and social media card

I would like 2 designs,

one with my logo that I have (attached file) for the front and then the chatterbook, Snapgallery and wanderguide icons on the back.I would like it to be eye catching.

The second design i would like the designers to come up with.I am looking for a colorful and eye catching but easy to read business card. I am in the center of Australia and would like earthy colors like orange/red, yellow, charcoal, brown, green etc. I would like a blue tongue lizard and a king brown snake in the design for the front. For the back I would like the Chatterbook, Snapgallery and wander guide logos.

Industry/Entity Type

Business

Contact Information for Business Card

Marcus Toller
CEO
GUM CREEK CRITTERS pty ltd
W: 041 907 2286
M: 048 216 0947
E: marcus@gumcreekcritters-example.com.au

Font styles to use
Other font styles liked:
• chiller

Colors
f37122
fbed22
ec1f27
474747
0492cd
acd036

Requirements
Must have
• Business name or my logo (attached file)
• Gum Creek Critters (in a cool font, like "chiller")
• Chatterbook icon
• Snapgallery icon
• Wanderguide icon
Nice to have
• Snake and a blue tongue lizard (either the full animals or just the heads)

```html
<!DOCTYPE html>
<html lang="en">
<head>
<meta charset="utf-8">
<title>Gum Creek Critters – Business Card</title>
<link rel="stylesheet" href="https://fonts.googleapis.com/css2?family=PT+Sans:wght@400;700&display=swap">
<style>
  :root {
    --stage: #000000;
    --card-light: #f3f3f3;
    --card-red: #d0263a;
    --brand-red: #cf2233;
    --ink: #333333;
    --white: #ffffff;
    --snake-orange: #d9582a;
    --snake-grey: #b9b4ae;
    --snake-dark: #2a2523;
  }
  * { margin: 0; padding: 0; box-sizing: border-box; }
  html, body {
    width: 1200px; height: 900px; overflow: hidden;
    background: var(--stage);
    font-family: "PT Sans", Arial, sans-serif;
  }
  .stage { position: relative; width: 1200px; height: 900px; }

  .card { position: absolute; top: 200px; width: 310px; height: 502px; overflow: hidden; }
  .card--front { left: 265px; background: var(--card-light); border-radius: 58px 0 58px 0; }
  .card--back  { left: 641px; background: var(--card-red);   border-radius: 0 58px 0 58px; }

  .brand-mark {
    position: absolute; left: 0; width: 100%;
    display: flex; align-items: center; justify-content: center; gap: 10px;
    font-weight: 700; text-transform: uppercase; letter-spacing: 1px;
    line-height: 1.05; text-align: left;
  }
  .brand-mark__dot { width: 22px; height: 22px; border-radius: 50%; flex: none; }
  .card--front .brand-mark { top: 100px; color: var(--brand-red); font-size: 30px; }
  .card--front .brand-mark__dot { background: var(--brand-red); }
  .card--back .brand-mark { top: 300px; color: var(--white); font-size: 34px; }
  .card--back .brand-mark__dot { background: var(--white); }

  .contact-person { position: absolute; left: 27px; top: 336px; }
  .contact-person__name { color: var(--brand-red); font-weight: 700; font-size: 18px; line-height: 22px; }
  .contact-person__role { color: var(--ink); font-size: 13px; line-height: 18px; }

  .contact-list { position: absolute; left: 27px; top: 402px; list-style: none; }
  .contact-list li {
    display: flex; align-items: center; gap: 9px;
    color: var(--ink); font-size: 13px; height: 21px;
  }
  .contact-list svg { width: 11px; height: 11px; fill: var(--brand-red); flex: none; }

  .feature-photo {
    position: absolute; left: 0; top: 22px; width: 100%; height: 165px;
    background: linear-gradient(120deg, var(--card-red) 0%, var(--snake-grey) 30%, var(--snake-orange) 55%, var(--snake-dark) 75%, var(--card-red) 100%);
    opacity: 0.85;
  }
</style>
</head>
<body>
<main class="stage">

  <section class="card card--front" aria-label="Business card front">
    <div class="brand-mark">
      <span class="brand-mark__dot"></span>
      <span>Gum Creek<br>Critters</span>
    </div>

    <div class="contact-person">
      <p class="contact-person__name">Marcus Toller</p>
      <p class="contact-person__role">CEO</p>
    </div>

    <ul class="contact-list">
      <li>
        <svg viewBox="0 0 24 24" aria-hidden="true"><path d="M6.6 10.8a15.1 15.1 0 0 0 6.6 6.6l2.2-2.2a1 1 0 0 1 1-.25 11.4 11.4 0 0 0 3.6.57 1 1 0 0 1 1 1V20a1 1 0 0 1-1 1A17 17 0 0 1 3 4a1 1 0 0 1 1-1h3.5a1 1 0 0 1 1 1c0 1.25.2 2.45.57 3.6a1 1 0 0 1-.25 1z"/></svg>
        041 907 2286
      </li>
      <li>
        <svg viewBox="0 0 24 24" aria-hidden="true"><path d="M5 2h14a1 1 0 0 1 1 1v18a1 1 0 0 1-1 1H5a1 1 0 0 1-1-1V3a1 1 0 0 1 1-1zm2 3v12h10V5zm5 13.5a1.2 1.2 0 1 0 0 2.4 1.2 1.2 0 0 0 0-2.4z"/></svg>
        048 216 0947
      </li>
      <li>
        <svg viewBox="0 0 24 24" aria-hidden="true"><path d="M2 5h20v14H2zm2 2v.5l8 5 8-5V7zm0 2.9V17h16V9.9l-8 5z"/></svg>
        marcus@gumcreekcritters-example.com.au
      </li>
    </ul>
  </section>

  <section class="card card--back" aria-label="Business card back">
    <div class="feature-photo" role="img" aria-label="Photograph of a banded red, grey and black snake coiling across the card"></div>
    <div class="brand-mark">
      <span class="brand-mark__dot"></span>
      <span>Gum Creek<br>Critters</span>
    </div>
  </section>

</main>
</body>
</html>
```